Website Design for Landscaping/Concrete Company

I need a website that is informative about what my company does and also offers before and after pictures of completed work. I already have a logo. The website must say "FREE ESTIMATES" somewhere and list a phone number. I would like to stick with the logo colors or similar (black and lime green).
Services Offered by Dornel Contractors:
Landscaping
Mowing
Concrete
Sidewalks
Brush Removal
Land Beautification

Please list the company name in large letters DORNEL CONTRACTORS
and also the contact information in large font.

Right now I am looking for a somewhat coverpage for my website. I don't have a lot of information for people to point and click on yet. Id like to get a coverpage to get my name out and then have a designer come back in a few months and update with more pictures and information.
Updates

If allowed please submit projects after due date. I made a mistake and only posted for one day. Thanks.

Coding

Coded - Design and coding required

```html
<!DOCTYPE html>
<html lang="en">
<head>
<meta charset="utf-8">
<title>Dornel Contractors</title>
<link href="https://fonts.googleapis.com/css2?family=Oswald:wght@400;500;600;700&family=Open+Sans:wght@400;600;700&display=swap" rel="stylesheet">
<style>
:root{
  --lime:#8cc63e;
  --lime-dark:#76ab2c;
  --ink:#111111;
  --charcoal:#1c1c1c;
  --text:#555555;
  --muted:#8a8a8a;
  --paper:#f4f4f2;
  --white:#ffffff;
}
*{box-sizing:border-box;margin:0;padding:0}
html,body{width:1200px;height:4376px;overflow:hidden}
body{font-family:"Open Sans",Arial,sans-serif;color:var(--text);background:var(--white);position:relative}
.abs{position:absolute}
.heading{font-family:"Oswald","Arial Narrow",sans-serif;text-transform:uppercase}
.btn{display:inline-block;background:var(--lime);color:var(--white);font-family:"Oswald","Arial Narrow",sans-serif;font-size:15px;letter-spacing:.5px;text-transform:uppercase;padding:12px 28px;white-space:nowrap}

/* header / hero */
.hero{top:0;left:0;width:1200px;height:720px;background:linear-gradient(180deg,#2a2a26 0%,#3d4a2a 40%,#6a5a36 70%,#2b2f20 100%)}
.hero-shade{top:0;left:0;width:1200px;height:720px;background:linear-gradient(90deg,rgba(0,0,0,.55),rgba(0,0,0,.1) 60%,rgba(0,0,0,.2))}
.topbar{top:0;left:0;width:1200px;height:58px;background:rgba(0,0,0,.55)}
.navbar{top:58px;left:0;width:1200px;height:34px;background:rgba(0,0,0,.75)}
.brand{top:18px;left:100px;display:flex;align-items:center;gap:12px}
.brand-mark{width:40px;height:40px;background:var(--lime)}
.brand-name{font-family:"Oswald",sans-serif;font-weight:600;font-size:22px;color:var(--white);letter-spacing:1px}
.top-contact{top:12px;left:770px;display:flex;align-items:center;gap:10px;color:var(--white)}
.top-contact small{display:block;font-size:11px;font-weight:700;letter-spacing:.5px}
.top-contact b{font-size:14px;color:var(--lime)}
.icon-circle{width:34px;height:34px;border-radius:50%;background:var(--lime);display:flex;align-items:center;justify-content:center}
.quote-btn{top:12px;left:1040px;padding:10px 18px;font-size:13px}
.nav{top:66px;left:500px;display:flex;gap:58px;font-family:"Oswald",sans-serif;font-size:15px;color:var(--white);letter-spacing:.5px}
.hero-title{top:170px;left:100px;font-size:44px;font-weight:700;color:var(--white);line-height:1.15}
.hero-sub{top:288px;left:100px;width:420px;font-size:14px;color:var(--white);line-height:1.5;font-weight:600}
.hero-cta{top:358px;left:100px;display:flex;align-items:center;gap:18px;color:var(--white)}
.hero-cta .or{width:30px;height:30px;border:1px solid var(--white);border-radius:50%;font-size:12px;display:flex;align-items:center;justify-content:center}
.hero-cta small{display:block;font-size:11px;font-weight:700}
.hero-cta b{font-size:17px;color:var(--lime)}

/* section headings */
.eyebrow{width:1200px;left:0;text-align:center;font-size:13px;color:var(--lime);font-weight:600;letter-spacing:.5px;text-transform:uppercase}
.boxed{left:50%;transform:translateX(-50%);border:3px solid var(--lime);padding:4px 28px;font-family:"Oswald",sans-serif;font-weight:700;font-size:40px;text-transform:uppercase;white-space:nowrap;line-height:1.2}

/* services */
.services{top:720px;left:0;width:1200px;height:800px;background:var(--paper)}
.explore{top:920px;left:0;width:1200px;text-align:center;font-size:16px;color:var(--text)}
.cards{top:960px;left:96px;display:flex;gap:24px}
.card{width:234px;height:368px;background:var(--white);box-shadow:0 2px 10px rgba(0,0,0,.1);position:relative;text-align:center}
.card .photo{height:170px}
.card h3{font-family:"Oswald",sans-serif;font-weight:600;font-size:19px;color:var(--ink);margin:22px 0 12px}
.card p{font-size:12px;line-height:1.6;padding:0 20px}
.card .go{position:absolute;bottom:-18px;left:99px;width:36px;height:36px;border-radius:50%;background:var(--lime);display:flex;align-items:center;justify-content:center}
.services-btn{top:1362px;left:517px}

/* about */
.about{top:1520px;left:0;width:1200px;height:620px;background:linear-gradient(180deg,#141414,#1d1f1a 60%,#121212)}
.about-photo{top:1700px;left:200px;width:440px;height:350px;background:linear-gradient(160deg,#9fb6c8 0%,#d9d6cc 35%,#5d8a2e 60%,#3e6a1e 100%)}
.about-text{top:1740px;left:660px;width:420px;color:#cfcfcf}
.about-text h2{font-family:"Oswald",sans-serif;font-weight:600;font-size:28px;color:var(--white);margin-bottom:16px}
.about-text p{font-size:13px;line-height:1.75;margin-bottom:22px}

/* projects */
.projects{top:2140px;left:0;width:1200px;height:980px;background:linear-gradient(180deg,#f3f3ef,#ecece6)}
.pair{width:492px;height:304px;display:flex;gap:4px}
.pair .shot{flex:1}
.swap{width:40px;height:40px;border-radius:50%;background:var(--white);box-shadow:0 1px 6px rgba(0,0,0,.3);display:flex;align-items:center;justify-content:center}
.projects-btn{top:3056px;left:506px}

/* contact */
.contact{top:3120px;left:0;width:1200px;height:720px;background:var(--white)}
.contact-title{top:3210px;left:0;width:1200px;text-align:center;font-size:54px;font-weight:700;color:var(--ink)}
.contact-rule{top:3244px;height:3px;width:150px;background:var(--lime)}
.contact-copy{top:3310px;left:210px;width:780px;text-align:center;font-size:16px;line-height:1.6}
.contact-copy b{color:var(--lime);font-size:20px}
.field{height:48px;background:var(--white);border:1px solid #dcdcdc;font-size:14px;color:var(--muted);padding:14px 16px;display:flex;align-items:center;gap:8px}
.form-bg{top:3392px;left:210px;width:780px;height:334px;background:#f1f1ee}
.send-btn{top:3660px;left:506px;padding:12px 32px}
.grass{top:3740px;left:0;width:1200px;height:100px;background:linear-gradient(180deg,rgba(255,255,255,0),#7fae3a 55%,#3f6e1d)}

/* footer */
.footer{top:3840px;left:0;width:1200px;height:536px;background:var(--ink)}
.foot-brand{top:3900px;left:100px;width:200px;text-align:center}
.foot-brand .brand-mark{margin:0 auto 16px;width:70px;height:70px}
.foot-brand .brand-name{font-size:22px}
.socials{top:4070px;left:110px;display:flex;gap:12px}
.socials span{width:28px;height:28px;border:1.5px solid var(--white);border-radius:50%}
.foot-col{top:3930px;color:#d0d0d0;font-size:15px}
.foot-col h4{font-family:"Oswald",sans-serif;font-weight:600;font-size:22px;color:var(--white);margin-bottom:14px}
.foot-col .bar{width:50px;height:3px;background:var(--lime);margin-bottom:20px}
.foot-col li{list-style:none;margin-bottom:14px;display:flex;align-items:center;gap:10px}
.foot-col .tick{width:6px;height:6px;background:var(--lime);border-radius:50%}
.foot-col .ic{width:36px;height:36px;border-radius:50%;background:var(--lime);display:flex;align-items:center;justify-content:center}
.copyright{top:4320px;left:0;width:1200px;border-top:1px solid #333;padding-top:18px;text-align:center;font-size:13px;color:#aaa}
</style>
</head>
<body>

<!-- HERO -->
<div class="abs hero" role="img" aria-label="Evening photo of a lit garden path and landscaped front yard"></div>
<div class="abs hero-shade"></div>
<div class="abs topbar"></div>
<div class="abs navbar"></div>
<div class="abs brand"><span class="brand-mark"></span><span class="brand-name">DORNEL CONTRACTORS</span></div>
<div class="abs top-contact">
  <span class="icon-circle"><svg width="16" height="16" viewBox="0 0 24 24" fill="#fff"><path d="M6.6 10.8a15.1 15.1 0 006.6 6.6l2.2-2.2a1 1 0 011-.24 11.4 11.4 0 003.6.57 1 1 0 011 1V20a1 1 0 01-1 1A17 17 0 013 4a1 1 0 011-1h3.5a1 1 0 011 1c0 1.25.2 2.45.57 3.57a1 1 0 01-.25 1z"/></svg></span>
  <div><small>FREE ESTIMATES</small><b>936-555-0142</b></div>
</div>
<div class="abs btn quote-btn">Request a Quote</div>
<nav class="abs nav"><span>HOME</span><span>ABOUT</span><span>SERVICES</span><span>WORK</span><span>CONTACT</span></nav>

<h1 class="abs heading hero-title">Serving all of East Texas<br>&amp; the Toledo Bend Area</h1>
<p class="abs hero-sub">Landscaping, mowing, concrete and brush removal for homes and businesses, done right from start to finish.</p>
<div class="abs hero-cta">
  <span class="btn">Get a Quote</span>
  <span class="or">OR</span>
  <span class="icon-circle"><svg width="16" height="16" viewBox="0 0 24 24" fill="#fff"><path d="M6.6 10.8a15.1 15.1 0 006.6 6.6l2.2-2.2a1 1 0 011-.24 11.4 11.4 0 003.6.57 1 1 0 011 1V20a1 1 0 01-1 1A17 17 0 013 4a1 1 0 011-1h3.5a1 1 0 011 1c0 1.25.2 2.45.57 3.57a1 1 0 01-.25 1z"/></svg></span>
  <div><small>CALL US TODAY</small><b>936-555-0142</b></div>
</div>

<!-- SERVICES -->
<section class="abs services"></section>
<div class="abs eyebrow" style="top:808px">Our Services</div>
<div class="abs boxed" style="top:832px;color:var(--ink)">What We Do</div>
<div class="abs explore">Explore all the ways we can help you</div>
<div class="abs cards">
  <div class="card"><div class="photo" role="img" aria-label="Green lawn with trees under a blue sky" style="background:linear-gradient(180deg,#a8c7e6 0%,#cfe0ee 40%,#5e9a32 60%,#3f7a20 100%)"></div><h3>General Contracting</h3><p>From start to finish we can help make your dream a reality. Whether big or small, our crew is ready to help.</p><span class="go"><svg width="14" height="14" viewBox="0 0 24 24" fill="none" stroke="#fff" stroke-width="3"><path d="M9 5l7 7-7 7"/></svg></span></div>
  <div class="card"><div class="photo" role="img" aria-label="Freshly mowed yard with trees" style="background:linear-gradient(180deg,#8c9aa6 0%,#6a7a60 45%,#4d7a2a 70%,#3a6220 100%)"></div><h3>Mowing &amp; Landscaping</h3><p>If you need help with your landscaping or lawn maintenance, we do it all. Contact us for mowing and planting.</p><span class="go"><svg width="14" height="14" viewBox="0 0 24 24" fill="none" stroke="#fff" stroke-width="3"><path d="M9 5l7 7-7 7"/></svg></span></div>
  <div class="card"><div class="photo" role="img" aria-label="Cleared driveway in front of a garage" style="background:linear-gradient(180deg,#d9d9d4 0%,#bfbdb4 50%,#8f8b80 100%)"></div><h3>Brush Removal</h3><p>We can rid you of unwanted brush and overgrowth quickly. Free quote to reclaim your property today.</p><span class="go"><svg width="14" height="14" viewBox="0 0 24 24" fill="none" stroke="#fff" stroke-width="3"><path d="M9 5l7 7-7 7"/></svg></span></div>
  <div class="card"><div class="photo" role="img" aria-label="Cleared and graded land site" style="background:linear-gradient(180deg,#b7d0e8 0%,#d8e3ea 40%,#a88a5e 65%,#8a6d45 100%)"></div><h3>Land Clearing &amp; Site Prep</h3><p>Offering a superior level of site preparation so you can turn your land into a beautiful space.</p><span class="go"><svg width="14" height="14" viewBox="0 0 24 24" fill="none" stroke="#fff" stroke-width="3"><path d="M9 5l7 7-7 7"/></svg></span></div>
</div>
<div class="abs btn services-btn">View All Services</div>

<!-- ABOUT -->
<section class="abs about"></section>
<div class="abs eyebrow" style="top:1570px;color:var(--white)">About Us</div>
<div class="abs boxed" style="top:1594px;font-size:26px;color:var(--white);padding:8px 26px">For Residential, Strata and Commercial Properties</div>
<div class="abs about-photo" role="img" aria-label="Home with a flowering front garden and green lawn"></div>
<div class="abs about-text">
  <h2>WELCOME TO DORNEL CONTRACTORS</h2>
  <p>We are a locally owned crew serving East Texas with landscaping, mowing, concrete and sidewalk work. Every job gets the same care, whether it is a small backyard or a large commercial lot. We show up on time, keep the site clean and stand behind our work. From brush removal to full land beautification, we turn rough ground into places you are proud of. Call today to set up your free estimate and see what we can do for you.</p>
  <span class="btn">Free Estimates</span>
</div>

<!-- PROJECTS -->
<section class="abs projects"></section>
<div class="abs eyebrow" style="top:2236px">Our Gallery</div>
<div class="abs boxed" style="top:2262px;color:var(--lime)">Recent Projects</div>

<div class="abs pair" style="top:2398px;left:100px"><div class="shot" role="img" aria-label="Before: bare dirt yard" style="background:linear-gradient(180deg,#5a6a3a,#8a7250)"></div><div class="shot" role="img" aria-label="After: new sod lawn" style="background:linear-gradient(180deg,#6a8a40,#4f7a2a)"></div></div>
<div class="abs swap" style="top:2530px;left:326px"><svg width="14" height="14" viewBox="0 0 24 24" fill="none" stroke="#333" stroke-width="3"><path d="M9 5l7 7-7 7"/></svg></div>
<div class="abs pair" style="top:2398px;left:608px"><div class="shot" role="img" aria-label="Before: overgrown lot" style="background:linear-gradient(180deg,#b8c4cc,#7a7a4a)"></div><div class="shot" role="img" aria-label="After: cleared graded lot" style="background:linear-gradient(180deg,#b9c9d6,#a88c62)"></div></div>
<div class="abs swap" style="top:2530px;left:834px"><svg width="14" height="14" viewBox="0 0 24 24" fill="none" stroke="#333" stroke-width="3"><path d="M9 5l7 7-7 7"/></svg></div>
<div class="abs pair" style="top:2718px;left:100px"><div class="shot" role="img" aria-label="Before: dense brush" style="background:linear-gradient(180deg,#8a9a7a,#5a6a4a)"></div><div class="shot" role="img" aria-label="After: cleared patio area" style="background:linear-gradient(180deg,#c9c9c2,#8a8a80)"></div></div>
<div class="abs swap" style="top:2850px;left:326px"><svg width="14" height="14" viewBox="0 0 24 24" fill="none" stroke="#333" stroke-width="3"><path d="M9 5l7 7-7 7"/></svg></div>
<div class="abs pair" style="top:2718px;left:608px"><div class="shot" role="img" aria-label="Before: unfinished kitchen" style="background:linear-gradient(180deg,#d8dce0,#a6acb2)"></div><div class="shot" role="img" aria-label="After: finished kitchen with cabinets" style="background:linear-gradient(180deg,#e6e8ea,#8e98a2)"></div></div>
<div class="abs swap" style="top:2850px;left:834px"><svg width="14" height="14" viewBox="0 0 24 24" fill="none" stroke="#333" stroke-width="3"><path d="M9 5l7 7-7 7"/></svg></div>
<div class="abs btn projects-btn">View All Projects</div>

<!-- CONTACT -->
<section class="abs contact"></section>
<div class="abs eyebrow" style="top:3182px">Get In Touch</div>
<div class="abs contact-rule" style="left:220px"></div>
<div class="abs contact-rule" style="left:830px"></div>
<h2 class="abs heading contact-title">Contact Us Today</h2>
<p class="abs contact-copy">Collaboration begins with a conversation. Whether you're interested in discussing a new project or simply wish to find out more about our services and what we can do for you, we are here to help.<br>Send us a message below or call us at <b>936-555-0142</b></p>
<div class="abs form-bg"></div>
<div class="abs field" style="top:3412px;left:232px;width:364px">&#128100; First Name*</div>
<div class="abs field" style="top:3412px;left:604px;width:364px">&#128100; Last Name*</div>
<div class="abs field" style="top:3472px;left:232px;width:364px">&#9993; Email*</div>
<div class="abs field" style="top:3472px;left:604px;width:364px">&#9742; Phone*</div>
<div class="abs field" style="top:3532px;left:232px;width:736px;height:110px;align-items:flex-start">&#9998; Message*</div>
<div class="abs btn send-btn" style="background:var(--charcoal)">Send Your Message</div>
<div class="abs grass" role="img" aria-label="Close-up of green grass"></div>

<!-- FOOTER -->
<footer class="abs footer"></footer>
<div class="abs foot-brand"><span class="brand-mark" style="display:block"></span><span class="brand-name">DORNEL CONTRACTORS</span></div>
<div class="abs socials"><span></span><span></span><span></span><span></span></div>
<div class="abs foot-col" style="left:340px"><h4>OUR SERVICES</h4><div class="bar"></div><ul><li>General Contracting</li><li>Mowing &amp; Landscaping</li><li>Brush Removal</li><li>Land Clearing &amp; Site Prep</li></ul></div>
<div class="abs foot-col" style="left:590px"><h4>QUICK LINKS</h4><div class="bar"></div><ul><li><span class="tick"></span>Home</li><li><span class="tick"></span>About</li><li><span class="tick"></span>Services</li><li><span class="tick"></span>Work</li><li><span class="tick"></span>Contact</li></ul></div>
<div class="abs foot-col" style="left:820px"><h4>USEFUL LINKS</h4><div class="bar"></div><ul>
  <li><span class="ic"><svg width="16" height="16" viewBox="0 0 24 24" fill="#fff"><path d="M6.6 10.8a15.1 15.1 0 006.6 6.6l2.2-2.2a1 1 0 011-.24 11.4 11.4 0 003.6.57 1 1 0 011 1V20a1 1 0 01-1 1A17 17 0 013 4a1 1 0 011-1h3.5a1 1 0 011 1c0 1.25.2 2.45.57 3.57a1 1 0 01-.25 1z"/></svg></span>936-555-0142</li>
  <li><span class="ic"><svg width="16" height="16" viewBox="0 0 24 24" fill="none" stroke="#fff" stroke-width="2"><rect x="3" y="5" width="18" height="14"/><path d="M3 6l9 7 9-7"/></svg></span>hello@dornelcontractors.example</li>
</ul></div>
<div class="abs copyright">© DORNEL CONTRACTORS All Rights Reserved 2020 | Privacy Policy | Terms of Use</div>

</body>
</html>
```